Brightly Fen business card for handing simple contact information and generating service awareness

Utilizing the attached logo(s), generate a professional, but approachable, card conveying a sense of capability and integrity. Please only use one logo of the four attached; the different colors are all acceptable, but preference will be given to a design integrating a teal/turquoise logo,

I do not know where to put in the contact information or details?

Target Market(s)

Agriculture, Farming, Timber, Forestry, Construction, Crane Service

Industry/Entity Type

Contact Information for Business Card

Name, Phone Number, email address

Colors

Designer to choose colors to be used in the design.

Requirements
Nice to have
• It would be great to have either a mountain or one of the attached cranes as a backdrop on the rear of the card. Simple watermarks and/or Debossing is also great

```html
<!DOCTYPE html>
<html lang="en">
<head>
<meta charset="utf-8">
<title>Brightly Fen – Business Card</title>
<link rel="stylesheet" href="https://fonts.googleapis.com/css2?family=Open+Sans:wght@400;600;700;800&display=swap">
<style>
  :root {
    --stage: #232323;
    --teal: #2a7064;
    --teal-deep: #1f5a50;
    --white: #ffffff;
  }
  * { margin: 0; padding: 0; box-sizing: border-box; }
  html, body {
    width: 1200px; height: 780px; overflow: hidden;
    background: var(--stage);
    font-family: "Open Sans", Arial, sans-serif;
  }
  .canvas { position: relative; width: 1200px; height: 780px; }

  .card {
    position: absolute;
    width: 560px; height: 320px;
    border-radius: 26px;
    overflow: hidden;
  }

  /* Back of card */
  .card-back {
    left: 50px; top: 50px;
    background: var(--teal);
    display: flex; align-items: center; justify-content: center;
  }
  .back-mark { display: flex; align-items: center; gap: 16px; }
  .back-mark .mark-dot {
    width: 46px; height: 46px; border-radius: 50%;
    background: var(--teal-deep);
  }
  .back-mark .brand-name {
    font-weight: 800; font-size: 44px; letter-spacing: 2px;
    color: var(--teal-deep); text-transform: uppercase;
  }

  /* Front of card */
  .card-front {
    left: 590px; top: 410px;
    background: var(--white);
  }
  .front-wave { position: absolute; inset: 0; width: 100%; height: 100%; }

  .front-mark {
    position: absolute; right: 30px; top: 48px;
    display: flex; align-items: center; gap: 10px;
  }
  .front-mark .mark-dot {
    width: 30px; height: 30px; border-radius: 50%;
    background: var(--teal);
  }
  .front-mark .brand-name {
    font-weight: 800; font-size: 26px; letter-spacing: 1px;
    color: var(--teal); text-transform: uppercase;
  }

  .contact {
    position: absolute; left: 34px; bottom: 18px;
    color: var(--white);
  }
  .contact .person-name { font-weight: 700; font-size: 22px; line-height: 1.1; }
  .contact .person-role { font-weight: 600; font-size: 13px; margin: 2px 0 8px 4px; }
  .contact .address { font-size: 12px; line-height: 1.4; margin: 0 0 8px 14px; }
  .contact .lines { list-style: none; margin-left: 14px; }
  .contact .lines li {
    display: flex; align-items: center; gap: 8px;
    font-size: 12px; line-height: 1.45;
  }
  .contact .lines svg { width: 12px; height: 12px; flex: none; }
</style>
</head>
<body>
<main class="canvas">

  <section class="card card-back" aria-label="Card back">
    <div class="back-mark">
      <span class="mark-dot"></span>
      <span class="brand-name">Brightly Fen</span>
    </div>
  </section>

  <section class="card card-front" aria-label="Card front">
    <svg class="front-wave" viewBox="0 0 560 320" preserveAspectRatio="none" aria-hidden="true">
      <path d="M0 152 C120 126 230 136 330 134 C430 132 500 116 560 90 L560 320 L0 320 Z" fill="var(--teal)"/>
      <path d="M50 144 C160 118 260 126 340 128 C420 129 490 118 525 104 C490 122 420 135 340 135 C260 135 160 128 50 144 Z" fill="var(--teal)"/>
      <path d="M230 136 C320 142 420 142 510 124 C430 148 320 150 230 136 Z" fill="var(--white)"/>
      <path d="M290 146 C380 154 460 150 530 136 C460 158 380 160 290 146 Z" fill="var(--white)"/>
    </svg>

    <div class="front-mark">
      <span class="mark-dot"></span>
      <span class="brand-name">Brightly Fen</span>
    </div>

    <div class="contact">
      <p class="person-name">Lena Marsh</p>
      <p class="person-role">Managing Director</p>
      <p class="address">418 Cedar Hollow Rd. Suite 120<br>Granbury, TX 76048</p>
      <ul class="lines">
        <li>
          <svg viewBox="0 0 24 24"><path fill="currentColor" d="M6.6 10.8a15 15 0 0 0 6.6 6.6l2.2-2.2a1 1 0 0 1 1-.25 11.4 11.4 0 0 0 3.6.57 1 1 0 0 1 1 1V20a1 1 0 0 1-1 1A17 17 0 0 1 3 4a1 1 0 0 1 1-1h3.5a1 1 0 0 1 1 1c0 1.25.2 2.45.57 3.6a1 1 0 0 1-.25 1z"/></svg>
          (555) 204-1187
        </li>
        <li>
          <svg viewBox="0 0 24 24"><path fill="currentColor" d="M2 5h20v14H2z M3.5 6.5v.4l8.5 6 8.5-6v-.4z" fill-rule="evenodd"/></svg>
          info@website.com
        </li>
        <li>
          <svg viewBox="0 0 24 24"><circle cx="12" cy="12" r="10" fill="none" stroke="currentColor" stroke-width="2"/><path d="M2 12h20M12 2c3 3 3 17 0 20M12 2c-3 3-3 17 0 20" fill="none" stroke="currentColor" stroke-width="1.6"/></svg>
          www.website.com
        </li>
      </ul>
    </div>
  </section>

</main>
</body>
</html>
```